Boring Fiberglass Repair Company needs creative business cards

The Fiberglass Repair industry isn't very fun or creative but we'd like a business card that communicates a fresh, modern, and service-oriented feel. We repair bathroom fixtures (bath tubs, showers, etc) which are made out of fiberglass. Our fiberglass repair service will be sold to bathtub manufacturers and also businesses that sell bathtubs. We will also offer our services to home owners that have broken showers and bathtubs.
Target Market(s)
Home builders, plumbing wholesalers, home owners
Contact Information for Business Card
Tag line: "Quality Craftsmanship Today"
Look and feel
Each slider illustrates characteristics of the customer's brand and the style your logo design should communicate.

```html
<!DOCTYPE html>
<html lang="en">
<head>
<meta charset="utf-8">
<title>Harbor Line Fiberglass – Business Cards</title>
<link href="https://fonts.googleapis.com/css2?family=Montserrat:wght@400;500;600;800&display=swap" rel="stylesheet">
<style>
  :root{
    --stage:#1e1e1f;
    --navy:#0b2550;
    --navy-deep:#08204a;
    --navy-light:#133a70;
    --emboss:#1d58b8;
    --red:#e0262b;
    --white:#ffffff;
  }
  *{margin:0;padding:0;box-sizing:border-box}
  html,body{width:1200px;height:900px;overflow:hidden;background:var(--stage)}
  body{font-family:"Montserrat",sans-serif;color:var(--white);position:relative}
  .card{
    position:absolute;left:280px;width:640px;height:366px;border-radius:22px;
    background:linear-gradient(135deg,var(--navy-deep) 0%,var(--navy) 55%,var(--navy-light) 100%);
    overflow:hidden;
  }
  .card--front{top:60px}
  .card--back{top:474px}

  /* front */
  .front-brand{
    position:absolute;top:118px;left:0;right:0;text-align:center;
    font-weight:800;font-size:44px;letter-spacing:1px;color:var(--emboss);line-height:1;
  }
  .front-brand small{display:block;margin-top:10px;font-size:17px;letter-spacing:14px;font-weight:800}
  .tagline-row{
    position:absolute;left:0;right:0;bottom:40px;display:flex;align-items:center;gap:16px;
  }
  .tagline-row .rule{flex:1;height:1px;background:var(--red)}
  .tagline{font-size:17px;font-weight:500;letter-spacing:1.5px;white-space:nowrap}

  /* back */
  .back-brand{
    position:absolute;left:36px;top:146px;width:230px;text-align:center;
    font-weight:800;font-size:24px;line-height:1;color:var(--white);letter-spacing:.5px;
  }
  .back-brand small{display:block;margin-top:8px;font-size:10px;letter-spacing:7px}
  .divider{position:absolute;left:292px;top:86px;width:2px;height:200px;background:var(--red)}
  .contact{position:absolute;left:318px;top:86px}
  .person-name{font-size:30px;font-weight:600;letter-spacing:1px;line-height:1}
  .person-name .first{color:var(--red)}
  .role{font-size:15px;font-weight:500;margin-top:6px}
  .address{font-size:15px;font-weight:500;line-height:1.35;margin-top:14px}
  .lines{list-style:none;margin-top:10px;font-size:15px;font-weight:500;line-height:1.4}
  .lines li{display:flex;align-items:center;gap:8px}
  .lines svg{width:11px;height:11px;flex:none}
</style>
</head>
<body>

<section class="card card--front" aria-label="Card front">
  <div class="front-brand">HARBOR LINE<small>FIBERGLASS</small></div>
  <div class="tagline-row">
    <span class="rule"></span>
    <span class="tagline">QUALITY CRAFTSMANSHIP TODAY</span>
    <span class="rule"></span>
  </div>
</section>

<section class="card card--back" aria-label="Card back">
  <div class="back-brand">HARBOR LINE<small>FIBERGLASS</small></div>
  <span class="divider"></span>
  <div class="contact">
    <p class="person-name"><span class="first">OWEN</span> CASTELL</p>
    <p class="role">Sales &amp; Marketing</p>
    <p class="address">118 Keel Street,<br>Riverton VIC 3310, Australia</p>
    <ul class="lines">
      <li><svg viewBox="0 0 12 12"><path d="M2.5 1l2 2-1 1.3c.6 1.4 1.7 2.5 3.1 3.1L7.9 6.4l2 2-1.3 1.6C5 9.6 2.4 7 1 3.5z" fill="none" stroke="var(--red)" stroke-width="1.2"/></svg>(03) 5550 0142</li>
      <li><svg viewBox="0 0 12 12"><rect x="1" y="2.5" width="10" height="7" fill="none" stroke="var(--red)" stroke-width="1.1"/><path d="M1 2.5l5 4 5-4" fill="none" stroke="var(--red)" stroke-width="1.1"/></svg>owen.castell@harborlinefiberglass.com</li>
      <li><svg viewBox="0 0 12 12"><circle cx="6" cy="6" r="4.8" fill="none" stroke="var(--red)" stroke-width="1.1"/><path d="M1.2 6h9.6M6 1.2c-2.4 3-2.4 6.6 0 9.6M6 1.2c2.4 3 2.4 6.6 0 9.6" fill="none" stroke="var(--red)" stroke-width="1"/></svg>harborlinefiberglass.com</li>
    </ul>
  </div>
</section>

</body>
</html>
```